Coastal Bright Sweep Business Card

We are a cleaning and waste management company with the slogan "making waste to landfill a thing of the past". We would like a re-design of our current business card. On the front we want to continue to use our logo as the focus point. On the back, we want the whole thing re-done to be less busy. We want the staff member’s name, the job title, mobile number, email and website. We do not want the address on the card. We still want the green, black and blue colours used, but a new font for the information on the back. Please do not change the logo design at all. We are also thinking about using icons to replace the text ‘mobile, email, website’. The “events + commercial” banner needs to be incorporated somewhere and needs to read “events + commercial + waste”. Another important point for consideration is that we are very concerned about being environmentally sustainable and will be printing on recycled paper. All designs should be made to compliment this in regards to boldness and colouring. Please find attached our logo, our colour chart and an image of our current business card.

```html
<!DOCTYPE html>
<html lang="en">
<head>
<meta charset="utf-8">
<title>Coastal Bright Sweep – Business Card</title>
<link rel="stylesheet" href="https://fonts.googleapis.com/css2?family=Source+Sans+3:wght@400;600;700&display=swap">
<style>
  :root {
    --backdrop: #2a2b2e;
    --navy: #2c5a93;
    --navy-deep: #244e84;
    --sky: #33ade3;
    --leaf: #7bbf3d;
    --ink: #555a60;
    --title-blue: #3c5fa8;
    --rule: #4a68b0;
    --paper: #ffffff;
  }
  html, body {
    margin: 0;
    width: 1200px;
    height: 900px;
    overflow: hidden;
    background: var(--backdrop);
    font-family: "Source Sans 3", sans-serif;
  }
  .canvas {
    position: relative;
    width: 1200px;
    height: 900px;
  }
  .card {
    position: absolute;
    left: 320px;
    width: 560px;
    height: 320px;
    box-shadow: 0 10px 30px rgba(0,0,0,.45);
    overflow: hidden;
  }
  .card--front {
    top: 100px;
    background: linear-gradient(135deg, var(--navy) 0%, var(--navy-deep) 100%);
    display: flex;
    align-items: center;
    justify-content: center;
  }
  .card--back {
    top: 480px;
    background: var(--paper);
  }
  .brand-name {
    margin: 0;
    font-weight: 700;
    color: var(--paper);
    font-size: 38px;
    letter-spacing: .5px;
    display: flex;
    align-items: center;
    gap: 12px;
  }
  .brand-name .brand-dot {
    width: 16px;
    height: 16px;
    border-radius: 50%;
    background: var(--leaf);
  }
  .card--back .brand-name {
    position: absolute;
    top: 34px;
    right: 30px;
    font-size: 22px;
    color: var(--sky);
    gap: 8px;
  }
  .card--back .brand-name .brand-dot {
    width: 10px;
    height: 10px;
  }
  .staff {
    position: absolute;
    left: 40px;
    top: 96px;
  }
  .staff__name {
    margin: 0;
    font-size: 28px;
    font-weight: 400;
    color: var(--ink);
    line-height: 1.1;
  }
  .staff__title {
    margin: 2px 0 0 18px;
    font-size: 16px;
    color: var(--title-blue);
  }
  .rule {
    width: 100px;
    height: 2px;
    background: var(--rule);
    margin: 12px 0 12px 22px;
  }
  .contact {
    list-style: none;
    margin: 0 0 0 22px;
    padding: 0;
  }
  .contact li {
    display: flex;
    align-items: center;
    gap: 8px;
    font-size: 14px;
    color: var(--ink);
    line-height: 22px;
  }
  .contact svg {
    width: 13px;
    height: 13px;
    flex: none;
  }
  .band {
    position: absolute;
    bottom: 0;
  }
  .band--blue {
    left: 0;
    width: 72%;
    height: 26px;
    background: var(--sky);
    display: flex;
    align-items: center;
    padding-left: 40px;
    box-sizing: border-box;
  }
  .services-banner {
    margin: 0;
    font-size: 13px;
    font-weight: 600;
    letter-spacing: 1.5px;
    text-transform: uppercase;
    color: var(--paper);
  }
  .band--green {
    right: 0;
    width: 27%;
    height: 34px;
    background: var(--leaf);
  }
</style>
</head>
<body>
<main class="canvas">

  <section class="card card--front" aria-label="Card front">
    <h1 class="brand-name"><span class="brand-dot"></span>Coastal Bright Sweep</h1>
  </section>

  <section class="card card--back" aria-label="Card back">
    <p class="brand-name"><span class="brand-dot"></span>Coastal Bright Sweep</p>

    <div class="staff">
      <h2 class="staff__name">Jordan Pellow</h2>
      <p class="staff__title">Client Manager</p>
      <div class="rule"></div>
      <ul class="contact">
        <li>
          <svg viewBox="0 0 16 16" aria-hidden="true"><path fill="#7bbf3d" d="M3 2h3l1.5 3.5-2 1.2a8 8 0 0 0 3.8 3.8l1.2-2L14 10v3a1 1 0 0 1-1 1A11 11 0 0 1 2 3a1 1 0 0 1 1-1z"/></svg>
          0400 555 218
        </li>
        <li>
          <svg viewBox="0 0 16 16" aria-hidden="true"><rect x="1" y="3" width="14" height="10" rx="1" fill="#7bbf3d"/><path d="M1.5 3.5 8 9l6.5-5.5" fill="none" stroke="#fff" stroke-width="1.3"/></svg>
          jpellow@coastalbrightsweep.com.au
        </li>
        <li>
          <svg viewBox="0 0 16 16" aria-hidden="true"><g fill="none" stroke="#7bbf3d" stroke-width="1.4"><circle cx="8" cy="8" r="6.3"/><ellipse cx="8" cy="8" rx="2.8" ry="6.3"/><path d="M1.7 8h12.6M3 4.5h10M3 11.5h10"/></g></svg>
          www.coastalbrightsweep.com.au
        </li>
      </ul>
      <div class="rule"></div>
    </div>

    <div class="band band--blue">
      <p class="services-banner">events + commercial + waste</p>
    </div>
    <span class="band band--green" aria-hidden="true"></span>
  </section>

</main>
</body>
</html>
```